Construction material supplies company business card ****

1. Full company name “K R Mortar Works Ltd”
I am after a Business card design for the company as a whole. We are better known in Solomon Islands as “K R Mortar” for short.

We are a building materials supplier of
Ready Mixed Concrete, Bricks and Blocks,
Quarry products- gravel, aggregates, sand etc.
Cement distributor/retailer of reputable brands.
Other prefab concrete products. Culverts, wave breakers, concrete retaining blocks etc.

2. Competitive Advantage over Competition: Quality, efficient, professional, dependable, reliable

3. We want people to feel trust worthy, high quality, strong when they see our brand

5. No preference to color. Maybe more sturdy and corporate. Not fancy.

Industry/Entity Type

CONSTRUCTION SUPPLY

Contact Information for Business Card

Name, Position, office phone mob phone, email

Requirements
Must have
• the company logo
Nice to have
• would like to see a mixture of designs, of with logo only and also with simple graphic designs to bring out the company whilst still have the strong sturdy professional feeling

```html
<!DOCTYPE html>
<html lang="en">
<head>
<meta charset="utf-8">
<title>K R Mortar Works Ltd — Business Card</title>
<link href="https://fonts.googleapis.com/css2?family=Roboto:wght@400;500;700&display=swap" rel="stylesheet">
<style>
  :root {
    --backdrop: #2b2b2b;
    --card-light: #e6e6e5;
    --card-mid: #d6d6d5;
    --ink: #1f3d63;
    --emboss: #bdbdbc;
  }
  * { box-sizing: border-box; margin: 0; padding: 0; }
  html, body { width: 1200px; height: 1138px; overflow: hidden; }
  body {
    background: var(--backdrop);
    font-family: "Roboto", Arial, sans-serif;
    color: var(--ink);
    position: relative;
  }
  .card {
    position: absolute;
    border-radius: 16px;
    background: radial-gradient(ellipse at 40% 35%, var(--card-light) 0%, var(--card-mid) 100%);
    overflow: hidden;
  }
  .card--front { left: 274px; top: 186px; width: 623px; height: 376px; }
  .card--back  { left: 276px; top: 608px; width: 618px; height: 374px; }

  .front-brand {
    position: absolute;
    left: 0; right: 0; top: 160px;
    text-align: center;
    font-weight: 700;
    font-size: 46px;
    letter-spacing: 2px;
    color: var(--emboss);
    text-transform: uppercase;
  }
  .front-web {
    position: absolute;
    left: 0; right: 0; top: 332px;
    text-align: center;
    font-size: 15px;
    letter-spacing: 7px;
    color: var(--ink);
    padding-left: 30px;
  }

  .holder { position: absolute; left: 46px; top: 42px; }
  .holder-name { font-weight: 700; font-size: 22px; line-height: 26px; }
  .holder-role { font-size: 15px; line-height: 20px; margin-top: 3px; }

  .contact-list { position: absolute; left: 48px; top: 201px; list-style: none; }
  .contact-item {
    display: flex; align-items: center;
    font-size: 15px; height: 26px;
  }
  .contact-icon { width: 14px; height: 14px; margin-right: 15px; fill: var(--ink); }
  .address { position: absolute; left: 46px; top: 283px; font-size: 15px; line-height: 26px; }

  .back-brand {
    position: absolute; left: 352px; top: 202px; width: 224px;
    text-align: center;
  }
  .brand-mark { width: 58px; height: 58px; background: var(--ink); margin: 0 auto 18px; }
  .brand-name {
    font-weight: 700; font-size: 31px; letter-spacing: 1px;
    text-transform: uppercase; white-space: nowrap;
  }
</style>
</head>
<body>
  <section class="card card--front" aria-label="Card front">
    <div class="front-brand">K R Mortar</div>
    <div class="front-web">www.krmortarworks.com</div>
  </section>

  <section class="card card--back" aria-label="Card back">
    <div class="holder">
      <div class="holder-name">Daniel Whitford</div>
      <div class="holder-role">Managing Director</div>
    </div>

    <ul class="contact-list">
      <li class="contact-item">
        <svg class="contact-icon" viewBox="0 0 16 16" aria-hidden="true"><path d="M1 5c0-2 3-3 7-3s7 1 7 3v1h-3V5H4v1H1z"/><path d="M3 7h10l1 7H2z"/></svg>
        000 0000 0000
      </li>
      <li class="contact-item">
        <svg class="contact-icon" viewBox="0 0 16 16" aria-hidden="true"><path d="M1 3h14v10H1z M2 4.2V12h12V4.2L8 9z"/><path d="M2 4l6 5 6-5z"/></svg>
        daniel@krmortarworks.com
      </li>
      <li class="contact-item">
        <svg class="contact-icon" viewBox="0 0 16 16" aria-hidden="true"><circle cx="8" cy="8" r="7"/><path d="M1 8h14M8 1c-3 3-3 11 0 14M8 1c3 3 3 11 0 14" stroke="#dedede" stroke-width="1" fill="none"/></svg>
        www.krmortarworks.com
      </li>
    </ul>

    <div class="address">234 Anywhere St., Any City,<br>Any Town, US 123456</div>

    <div class="back-brand">
      <div class="brand-mark" aria-hidden="true"></div>
      <div class="brand-name">K R Mortar</div>
    </div>
  </section>
</body>
</html>
```